Maplers Report Design for Senior Care REIT

We have pulled high-level summary information from a Mapler Report, and compiled what we care about into the attached document. We would like you to take the information in the document and create a visual sheet, flyer, or slide deck (option to best layout based on info and creative vision). This should be QVN branded (logo attached) and should reflect design elements and vibes that you see on (qvnreit.example). This visual is for our executive team and should be extremely easy to read with engaging visuals for the stats included. Please include a cover page.

Target Market(s)

Corporate Executive Team

Industry/Entity Type

Senior Housing

Other font styles liked:
• Canada Type Gibson

Colors
0054AA
0677BA
7BADD7
CADEEF
E8F1F8

Requirements
Must have
• QVN branding, include all information on provided doc

```html
<!DOCTYPE html>
<html lang="en">
<head>
<meta charset="utf-8">
<title>Maplers Report – Senior Care REIT</title>
<link href="https://fonts.googleapis.com/css2?family=Figtree:wght@300;400;600;700;800&display=swap" rel="stylesheet">
<style>
:root{
  --navy:#0a3291;
  --blue:#0054aa;
  --mid:#0677ba;
  --sky:#7badd7;
  --pale:#cadeef;
  --mist:#e8f1f8;
  --sheet:#a3a3a3;
  --ink:#1a1a1a;
  --black:#0d0d0d;
}
*{box-sizing:border-box;margin:0;padding:0}
html,body{width:843px;height:1200px;overflow:hidden}
body{background:var(--sheet);font-family:"Figtree",sans-serif;color:var(--ink);position:relative}
.slide{position:absolute;width:385px;height:217px;background:#fff;overflow:hidden}
.col-l{left:29px}.col-r{left:429px}
.row1{top:29px}.row2{top:260px}.row3{top:491px}.row4{top:722px}.row5{top:954px}
.photo{position:absolute;inset:0}
.photo-warm{background:linear-gradient(160deg,#6b7aa3 0%,#b98b8f 35%,#7a4a3e 65%,#3b3f4a 100%)}
.photo-lobby{background:linear-gradient(140deg,#d9d4cc 0%,#8a7a68 45%,#3d3a3a 80%,#6c7890 100%)}
.photo-living{background:linear-gradient(150deg,#cfc8bb 0%,#a89f8f 40%,#6f6a66 75%,#5b6a80 100%)}
.photo-house{background:linear-gradient(170deg,#9fb2c9 0%,#c7cfd6 40%,#7c8ea4 70%,#4e7a3c 100%)}
.photo-blue{background:linear-gradient(175deg,#1d5fbf 0%,#3f7fd0 45%,#9a9086 70%,#4f6e3a 100%)}
.photo-night{background:linear-gradient(170deg,#3567b5 0%,#2e4a78 40%,#5c5550 70%,#252525 100%)}
.deco{position:absolute;inset:0;width:100%;height:100%}
.brand{position:absolute;display:flex;align-items:center;gap:5px;color:var(--navy);font-weight:800;letter-spacing:.5px}
.brand i{display:block;background:var(--navy)}
.footer{position:absolute;left:0;right:0;height:10.5px;color:#fff;font-size:5.5px;letter-spacing:1.6px;display:flex;align-items:center;justify-content:center}
.footer.dark{bottom:0;background:var(--black)}
.footer.blue{top:200px;background:var(--blue)}
.footer .mini{position:absolute;right:8px;display:flex;align-items:center;gap:2px;font-weight:800;font-size:5px;letter-spacing:.3px}
.footer .mini i{width:5px;height:5px;background:#fff;display:block}
.body{font-size:8.6px;line-height:11.6px;font-weight:300}
.group-title{font-size:16.5px;font-weight:700;letter-spacing:.3px;color:var(--ink);display:flex;align-items:center;gap:7px}
.marker{width:9px;height:9px;background:var(--blue);display:inline-block;flex:none}
.groups{list-style:none;margin-top:5px}
.groups li{font-size:9px;font-weight:600;display:flex;align-items:center;gap:7px;height:15.6px}
.groups .marker{width:6px;height:6px}
.callout{position:absolute;background:var(--mid);color:#fff;font-size:7.6px;font-weight:600;line-height:10.2px;display:flex;align-items:center}
.small{font-size:6.9px;line-height:8.6px;font-weight:300}
.list{list-style:none}
.list li{position:relative;padding-left:6px;font-size:7px;line-height:8.4px;font-weight:300;margin-bottom:1.7px}
.list li::before{content:"›";position:absolute;left:0;top:-1px;color:var(--mid);font-weight:700;font-size:8px}
.list li b{font-weight:600}
.list.tight li{font-size:6.8px}
.heading{font-size:7.6px;font-weight:700;line-height:9.6px}
.stat{position:absolute;top:104px;width:106px;height:87px;color:#fff;font-size:8.6px;line-height:11.5px;font-weight:300;padding:8px 8px}
.stat b{font-weight:700}
</style>
</head>
<body>

<section class="slide col-l row1">
  <div class="photo photo-warm" role="img" aria-label="Senior care centre exterior at dusk" style="clip-path:polygon(0 0,100% 0,100% 168px,0 168px)"></div>
  <svg class="deco" viewBox="0 0 385 217" preserveAspectRatio="none" aria-hidden="true">
    <polygon points="0,40 0,168 60,168" fill="#fff" opacity=".95"/>
    <polygon points="0,128 0,217 385,217 385,168 110,168 60,128" fill="#fff"/>
    <line x1="60" y1="128" x2="185" y2="0" stroke="#fff" stroke-width="3"/>
    <line x1="190" y1="0" x2="360" y2="168" stroke="#fff" stroke-width="3"/>
  </svg>
  <div class="brand" style="left:18px;top:160px;font-size:20px"><i style="width:22px;height:22px"></i>QVN REIT</div>
  <div style="position:absolute;left:147px;top:176px;color:var(--mid);line-height:12px">
    <div style="font-size:12.5px;font-weight:400;letter-spacing:.3px">MAPLERS REPORT</div>
    <div style="font-size:17px;font-weight:300">SENIOR CARE</div>
  </div>
  <div style="position:absolute;left:272px;top:176px;font-size:37px;font-weight:800;color:var(--navy);line-height:32px;letter-spacing:1px">REIT</div>
</section>

<section class="slide col-r row1">
  <div class="photo photo-warm" role="img" aria-label="Senior care centre exterior at dusk" style="clip-path:polygon(255px 0,100% 0,100% 100%,130px 100%)"></div>
  <svg class="deco" viewBox="0 0 385 217" preserveAspectRatio="none" aria-hidden="true">
    <polygon points="169,0 262,0 225,55" fill="var(--blue)"/>
    <line x1="226" y1="54" x2="128" y2="206" stroke="var(--sky)" stroke-width="3"/>
  </svg>
  <div class="brand" style="left:22px;top:30px;font-size:19px"><i style="width:22px;height:22px"></i>QVN REIT</div>
  <div class="body" style="position:absolute;left:22px;top:83px;width:150px">
    <b style="font-weight:600">Respondents were categorized</b> in one of three groups based on their likelihood of moving to an <b style="font-weight:600">age-qualified community</b> in the future:
  </div>
  <ul class="groups" style="position:absolute;left:22px;top:144px">
    <li><span class="marker"></span>PROBABLES</li>
    <li><span class="marker"></span>POSSIBLES</li>
    <li><span class="marker"></span>IMPROBABLES</li>
  </ul>
  <div class="footer dark">COPYRIGHT 2024 - QVN REIT</div>
</section>

<section class="slide col-l row2">
  <div class="photo photo-lobby" role="img" aria-label="Lobby with round table and armchairs" style="clip-path:polygon(0 0,115px 0,252px 100%,0 100%)"></div>
  <svg class="deco" viewBox="0 0 385 217" preserveAspectRatio="none" aria-hidden="true">
    <polygon points="122,0 216,0 162,55" fill="var(--blue)"/>
    <line x1="160" y1="55" x2="258" y2="206" stroke="var(--sky)" stroke-width="3"/>
  </svg>
  <div class="brand" style="left:266px;top:30px;font-size:19px"><i style="width:22px;height:22px"></i>QVN</div>
  <div class="group-title" style="position:absolute;right:24px;top:86px"><span class="marker"></span>PROBABLES</div>
  <p class="body" style="position:absolute;right:24px;top:113px;width:130px;text-align:right">Respondents who were likely or very likely to move to a residential community with services where the permanent residents must be a minimum of 55 years of age.</p>
  <div class="footer dark">COPYRIGHT 2024 - QVN REIT</div>
</section>

<section class="slide col-r row2">
  <div class="photo photo-house" role="img" aria-label="Community clubhouse with covered entrance" style="clip-path:polygon(262px 0,100% 0,100% 100%,130px 100%)"></div>
  <svg class="deco" viewBox="0 0 385 217" preserveAspectRatio="none" aria-hidden="true">
    <polygon points="169,0 262,0 225,55" fill="var(--blue)"/>
    <line x1="226" y1="54" x2="128" y2="206" stroke="var(--sky)" stroke-width="3"/>
  </svg>
  <div class="brand" style="left:26px;top:30px;font-size:19px"><i style="width:22px;height:22px"></i>QVN</div>
  <div class="group-title" style="position:absolute;left:26px;top:86px"><span class="marker"></span>POSSIBLES</div>
  <p class="body" style="position:absolute;left:25px;top:113px;width:122px">Respondents who were unsure if they would move to a residential community where the permanent residents must be a minimum of 55 years of age.</p>
  <div class="footer dark">COPYRIGHT 2024 - QVN REIT</div>
</section>

<section class="slide col-l row3">
  <div class="photo photo-living" role="img" aria-label="Bright living room with sofa and coffee table" style="clip-path:polygon(0 0,115px 0,252px 100%,0 100%)"></div>
  <svg class="deco" viewBox="0 0 385 217" preserveAspectRatio="none" aria-hidden="true">
    <polygon points="122,0 216,0 162,55" fill="var(--blue)"/>
    <line x1="160" y1="55" x2="258" y2="206" stroke="var(--sky)" stroke-width="3"/>
  </svg>
  <div class="brand" style="left:266px;top:30px;font-size:19px"><i style="width:22px;height:22px"></i>QVN</div>
  <div class="group-title" style="position:absolute;right:24px;top:86px"><span class="marker"></span>IMPROBABLES</div>
  <p class="body" style="position:absolute;right:19px;top:113px;width:140px;text-align:right">Respondents who were unlikely or very unlikely to move to a residential community where the permanent residents must be a minimum of 55 years of age</p>
  <div class="footer dark">COPYRIGHT 2024 - QVN REIT</div>
</section>

<section class="slide col-r row3">
  <div class="photo photo-lobby" role="img" aria-label="Sunlit lounge with pedestal table and vase" style="clip-path:polygon(0 0,193px 0,130px 100%,0 100%)"></div>
  <div class="small" style="position:absolute;left:205px;top:22px;width:160px">The top five in-unit amenities ranked by all respondents were full kitchen (refrigerator, stove/oven, microwave); laundry room with washer/dryer; living room or great room; lots of windows for plenty of natural light; and additional storage space for seasonal or occasionally used items.</div>
  <div class="heading" style="position:absolute;left:205px;top:93px;width:160px">Most preferred location among Probables and Possibles:</div>
  <div class="callout" style="left:122px;top:120px;width:238px;height:49px;padding:0 10px 0 18px;clip-path:polygon(14px 0,100% 0,100% 100%,0 100%)">Outlying suburban (outer edge developed areas of a city where there are more single-family homes and neighborhoods and fewer commercial areas) (43%)</div>
  <div class="footer blue">COPYRIGHT 2024 - QVN REIT<span class="mini"><i></i>QVN</span></div>
</section>

<section class="slide col-l row4">
  <div class="photo photo-night" role="img" aria-label="Residential building exterior at dusk" style="clip-path:polygon(175px 0,100% 0,100% 200px,253px 200px)"></div>
  <div class="heading" style="position:absolute;left:23px;top:22px;width:160px">59% of Probables &amp; Possibles rated the following as essential or desirable:</div>
  <ul class="list" style="position:absolute;left:23px;top:46px;width:150px">
    <li>Full kitchen with refrigerator, stove/oven and microwave</li>
    <li>Laundry room with washer/dryer</li>
    <li>Living room or great room</li>
    <li>Lots of windows for plenty of natural light</li>
    <li>Additional storage space for seasonal or occasionally used items</li>
    <li>Fiber-Optic Internet/Gigabit Internet</li>
    <li>Walk-in closet</li>
    <li>Open porch, patio, or balcony</li>
    <li>Dining area in the kitchen</li>
    <li>Screened porch, patio, or balcony</li>
    <li>Study or den</li>
    <li>Enclosed porch, patio, or balcony</li>
  </ul>
  <div class="callout" style="left:162px;top:123px;width:171px;height:46px;padding:0 16px 0 11px">55% and 61% of Probables and Possibles, respectively, would prefer to receive care “In my residence”</div>
  <div class="footer blue">COPYRIGHT 2024 - QVN REIT<span class="mini"><i></i>QVN</span></div>
</section>

<section class="slide col-r row4">
  <div class="photo photo-blue" role="img" aria-label="Community building under a clear blue sky" style="clip-path:polygon(0 0,157px 0,85px 200px,0 200px)"></div>
  <div class="heading" style="position:absolute;left:161px;top:22px;width:200px">“Desirable + essential” preferences for common area amenities among Probables &amp; Possibles:</div>
  <ul class="list" style="position:absolute;left:161px;top:49px;width:100px">
    <li><b>Walking trails 64%</b></li>
    <li><b>On-site storage units 55%</b></li>
    <li><b>Indoor fitness center 54%</b></li>
    <li><b>Activity room 52%</b></li>
    <li><b>Convenience store 52%</b></li>
    <li><b>A family-friendly lounge 52%</b></li>
    <li><b>ATM 50%</b></li>
    <li>Multi-purpose room: group meetings, classes, card room, etc. 49%</li>
  </ul>
  <ul class="list" style="position:absolute;left:266px;top:49px;width:105px">
    <li>Library 47%</li>
    <li>Indoor swimming pool 46%</li>
    <li>Beauty salon/barbershop 45%</li>
    <li>Visiting doctor's clinic 42%</li>
    <li>Indoor running/walking track 41%</li>
    <li>Media room/movie room 41%</li>
    <li>Outdoor grilling stations 40%</li>
  </ul>
  <div class="footer blue">COPYRIGHT 2024 - QVN REIT<span class="mini"><i></i>QVN</span></div>
</section>

<section class="slide col-l row5">
  <div class="photo photo-lobby" role="img" aria-label="Sunlit lounge with pedestal table and vase" style="clip-path:polygon(225px 0,100% 0,100% 200px,255px 200px)"></div>
  <div class="heading" style="position:absolute;left:19px;top:22px;width:210px">“Desirable + essential” preferences for common area amenities among Probables &amp; Possibles broken up by age group (55-74 – 75+):</div>
  <ul class="list tight" style="position:absolute;left:19px;top:56px;width:121px">
    <li><b>Walking trails 67% – 59%</b></li>
    <li><b>Indoor fitness center 55% – 52%</b></li>
    <li><b>On-site storage units 54% – 56%</b></li>
    <li><b>Activity room 52% – 52%</b></li>
    <li><b>ATM 51% – 48%</b></li>
    <li><b>Convenience store 51% – 52%</b></li>
    <li>A family-friendly lounge 49% – 56%</li>
    <li>Indoor swimming pool 48% – 42%</li>
    <li>Multi-purpose room: group meetings, classes, card room, etc. 47% – 51%</li>
  </ul>
  <ul class="list tight" style="position:absolute;left:143px;top:56px;width:92px">
    <li>Outdoor grilling stations 45% – 34%</li>
    <li>Library 44% – 51%</li>
    <li>Outdoor swimming pool 44% – 30%</li>
    <li>Beauty salon/barbershop 43% – 49%</li>
    <li>Indoor running/walking track 43% – 38%</li>
    <li>Visiting doctor's clinic 42% – 42%</li>
  </ul>
  <div class="footer blue">COPYRIGHT 2024 - QVN REIT<span class="mini"><i></i>QVN</span></div>
</section>

<section class="slide col-r row5" style="background:var(--mist)">
  <svg class="deco" viewBox="0 0 385 217" preserveAspectRatio="none" aria-hidden="true">
    <g fill="#fff" opacity=".75">
      <polygon points="20,0 60,0 -40,217 -80,217"/>
      <polygon points="110,0 150,0 50,217 10,217"/>
      <polygon points="260,0 300,0 400,217 360,217"/>
      <polygon points="340,0 380,0 480,217 440,217"/>
    </g>
  </svg>
  <div class="brand" style="left:148px;top:30px;font-size:22px"><i style="width:24px;height:24px"></i>QVN</div>
  <div class="stat" style="left:23px;background:var(--navy)">29% of Possibles &amp; Probables considered it essential and 35% considered themselves indifferent to having a pet-friendly community</div>
  <div class="stat" style="left:139px;background:var(--mid)">69% of Possibles &amp; Probables prefer Dining Out as a desired activity <b>(community proximity to restaurants is a must)</b></div>
  <div class="stat" style="left:256px;background:#5b9bd5">58% of Possibles &amp; Probables desire local travel as a possible activity (47% desire travel US &amp; abroad)</div>
  <div class="footer blue">COPYRIGHT 2024 - QVN REIT<span class="mini"><i></i>QVN</span></div>
</section>

</body>
</html>
```